Complete Stationary Package Needed for New Dental Office ! ! !

I'm moving my dental office and would like to use my existing logo to create a new:
- Business Card (please submit Business Card designs to this project - http://tasks.artbidhub.example/task.aspx?id=514290)
- Appointment Card (submit here)
- Letterhead (submit here)
- Envelope (submit here)
My practice name (within my logo) is:
Melvin R. Tuttle, D.D.S., P.A.
Family and Cosmetic Dentistry
***Obviously you will notice that the lower leg of the "T" in my logo is a smile.
My new address and contact information is:
340 Larkspur Commons Drive, Suite 118
Cary, NC 27593
919-472-3081 (ph)
919-472-3095 (fax)
info@tuttledds.example
www.tuttledds.example
If you would like to use a tagline, I would suggest "Precision Dentistry with a Personal Touch".
I have attached my logo in numerous formats.
I have also attached 2 QR codes, one of which links to my website and the other one which links to a "Like" page for my business Chatterly page. These QR codes could be improved by putting a graphic in the middle, but I created these myself and did not know how to do this.
Thank you for your time. I look forward to seeing all of your creative ideas!
Depending on the designs, I may award 2 different winners for the Business Card project and the Stationery Project. Or if a design is really good, I will award both projects to the same designer.
Updates
Project Deadline Extended
Reason: PixelBazaar administrators recently helped me split my project into 2 projects - 1 for business card and 1 for letterhead, envelope, etc. and I would like sufficient time to receive designs and provide feedback. Thank you.
Target Market(s)
Current and prospective dental patients.
Industry/Entity Type
Dental
Requirements
Must have
- Please ensure business card has a 2-sided design.
- Please ensure that your design is "practical" for printing purposes.
Nice to have
- Improvement of QR codes by addition of graphics in the middle to differentiate them. Incorporation of QR codes into business card design, maybe on the back side? I would consider the Chatterly QR code more important than the website QR code simply because my website URL is very easy to type.
Should not have
- Please, NO "floating" or "extracted" teeth which sends an undesirable message.

```html
<!DOCTYPE html>
<html lang="en">
<head>
<meta charset="utf-8">
<title>Melvin R. Tuttle, D.D.S., P.A. — Appointment Card</title>
<link rel="stylesheet" href="https://fonts.googleapis.com/css2?family=Cinzel:wght@500&family=Open+Sans:wght@300;400&display=swap">
<style>
  :root {
    --backdrop-top: #c4c4c4;
    --backdrop-bottom: #9e9e9e;
    --teal: #13b2ad;
    --teal-deep: #0e9a96;
    --navy-ink: #16305a;
    --royal: #3b4fa8;
    --royal-deep: #2e3f92;
    --frame: rgba(255,255,255,0.75);
    --field: #f7f7f9;
    --mark: #1f3a6b;
  }
  * { box-sizing: border-box; margin: 0; padding: 0; }
  html, body { width: 1200px; height: 1091px; overflow: hidden; }
  body {
    background: linear-gradient(180deg, var(--backdrop-top), var(--backdrop-bottom));
    font-family: "Open Sans", Arial, sans-serif;
    position: relative;
  }
  .card {
    position: absolute;
    top: 212px;
    width: 440px;
    height: 667px;
    border-radius: 22px;
    box-shadow: 0 12px 30px rgba(0,0,0,0.25);
    overflow: hidden;
  }
  .card::before {
    content: "";
    position: absolute;
    inset: 12px;
    border: 2px solid var(--frame);
    border-radius: 14px;
    pointer-events: none;
  }
  /* Front */
  .card-front {
    left: 120px;
    background: linear-gradient(180deg, var(--teal), var(--teal-deep));
    text-align: center;
  }
  .brand-square {
    position: absolute;
    left: 175px;
    top: 66px;
    width: 90px;
    height: 90px;
    background: var(--mark);
  }
  .practice-name {
    position: absolute;
    top: 300px;
    left: 0; right: 0;
    font-family: "Cinzel", Georgia, serif;
    font-weight: 500;
    font-size: 21px;
    letter-spacing: 0.5px;
    color: var(--navy-ink);
  }
  .practice-tagline {
    position: absolute;
    top: 330px;
    left: 0; right: 0;
    font-family: "Cinzel", Georgia, serif;
    font-weight: 500;
    font-size: 12px;
    letter-spacing: 1px;
    color: var(--navy-ink);
  }
  .practice-tagline span {
    display: inline-block;
    border-top: 1px solid var(--navy-ink);
    padding: 2px 10px 0;
  }
  .address {
    position: absolute;
    bottom: 78px;
    left: 0; right: 0;
    font-size: 15px;
    line-height: 1.45;
    color: var(--navy-ink);
  }
  /* Back */
  .card-back {
    left: 640px;
    background: linear-gradient(180deg, var(--royal), var(--royal-deep));
    color: #fff;
    padding: 46px 44px 0;
  }
  .card-title {
    font-weight: 300;
    font-size: 30px;
    letter-spacing: 0.5px;
    text-transform: uppercase;
    text-align: center;
    border-bottom: 2px solid #fff;
    padding-bottom: 2px;
    margin: 0 6px 8px;
  }
  .field-label {
    font-weight: 300;
    font-size: 31px;
    line-height: 1.2;
    margin-top: 6px;
  }
  .field {
    background: var(--field);
    border-radius: 12px;
    height: 48px;
    margin-top: 2px;
    box-shadow: inset 0 2px 4px rgba(0,0,0,0.12);
  }
  .field-large { height: 152px; border-radius: 16px; }
  .contact {
    margin-top: 30px;
    text-align: center;
    font-size: 15px;
    line-height: 1.45;
    color: rgba(255,255,255,0.85);
  }
</style>
</head>
<body>
  <section class="card card-front" aria-label="Appointment card front">
    <div class="brand-square"></div>
    <div class="practice-name">Melvin R. Tuttle, D.D.S., P.A.</div>
    <div class="practice-tagline"><span>Family and Cosmetic Dentistry</span></div>
    <p class="address">340 Larkspur Commons Drive,<br>Suite 118, Cary, NC 27593</p>
  </section>

  <section class="card card-back" aria-label="Appointment card back">
    <h1 class="card-title">Appointment Card</h1>
    <div class="field-label">Date</div>
    <div class="field"></div>
    <div class="field-label">Time</div>
    <div class="field"></div>
    <div class="field-label">Reason</div>
    <div class="field field-large"></div>
    <p class="contact">Tel. 919-472-3081<br>Fax. 919-472-3095</p>
  </section>
</body>
</html>
```